Flyer for an pediatric sleep consultancy - to distribute to play and childcare centers etc.

I need a flyer that will attract the attention of parents with children between the age of babies to toddlers, who may be experiencing sleep issues. The flyer will be placed at places such as community centers, doctors room, play centers, kindergardens, etc.

My company is called "The Quiet Meadow Studio" and provides a sleep consultancy service. My service essentially provides a customized plan for parents to follow and general advice and guidance. It is not medical advice.

I like to the flyer to have an overall tone that is soft and peaceful with a clean and beautiful design, however can catch the attention of parents who may be struggling with their child's sleep issues and are sleep deprived. I would like photos with minimal text. The colour I use is a brownish rose. I will attach some of my designs to give you an idea. You can have a look at my homepage as well to get an idea about my esthetic direction and the colour. Although the colour of my page is a bit too brownish....

I will provide the text to appear in the flyer once I have a better idea of the layout that I prefer for the flyer. The text however wont be extensive, just some catchy points.

I want to direct people to my website which is www.quietmeadowstudio-example.com
I offer a first FREE evaluation call, to the parents, to get to know each other better, learn about their child's particular sleep problems and see if we are a good fit and can work together. I would like to have this information somehow on the flyer, so that the parents will contact me.
I also have a facebook page, which is: The Quiet Meadow Studio

I have a logo that I would like to appear on the flyer. I will attach the file once the uploader on art bazaar is fixed.

When I print the flyer - I like to print A5 SIZE ... please make sure the formatting is OK for this size.

Here are some text ideas. of course all of it would be too much, I guess. On the front of the flyer I would like to have some catchy phrase or something similar to get people interested and to want to know more. On the back there could be a bit more text and information. But I'm open too suggestions....
I'm not too sure about the wording yet. But here are some text that I might be use:

Is sleep an issue in your home?

Is your baby having trouble sleeping? ... are you?!
I can help!

Sleep, baby, sleep….

Teaching children how to sleep

The Quiet Meadow Studio is a pediatric sleep consultancy that specializes in helping parents with children who struggle to develop good and healthy sleep habits.
Disruptive sleep patterns or not enough sleep can affect the physical, mental and emotional development of your child.

Of course nobody plans to have a sleep problem, but habits can become easily ingrained and spiral quickly out of control and you can find yourself sleep deprived, desperate and not too sure what to do. You see all the other sleeping babies and wish there was someone who understood what you were going through?! Well, there is!

Contact me for a free 15 minute consultation.

This 15 minute „mini“ consultation is a chance to discuss your unique sleep challenges and sleep goals with me. I will provide you with an overview of how I will work with your family to achieve your wildest sleep dreams (goals).
Furthermore do I understand and believe that every child and their family is unique and there is no one size fits all!
I would love to have a chat with you and talk about how I can help make things easier for you and your family!

Do I need a sleep consultant for my child?
The answer is yes if:
- if your child will only fall asleep when nursing or bottle feeding
- if your child needs a dummy or other external aid, like being rocked, patted or taken for a care ride to fall asleep
- if your good night routine is a challenging and exhausting procedure instead of a relaxed and enjoyable moment for the whole family
- if sleep is a constant battle in your home which leaves you feeling frustrated and exhausted
- if your own lack of sleep is taking a toll on you and the whole family

What can I do for you?

I will:

- Guide you to set an age appropriate foundation for good sleep
- Create an individual sleep plan tailored especially to your child’s sleep needs and circumstances
- Help you to teach your childto go to sleep and get back to sleep independently during the night
- show you how to teach your child to take healthful, restorative naps
-Learn

Contact:

Marta Lindqvist
info@quietmeadowstudio-example.com
www.quietmeadowstudio-example.com
+34 612 380 574

Consultations in English, German or Spanish via Phone/Skype or home consultation

Reason: I have to go on a business trip and won't be able to choose a design until the deadline. During the trip I won't have time to give feedback and ask for changes. thank you

Target Market(s)

parents, sleep deprived mothers, young families, child care provider,

Industry/Entity Type

Baby Care

Contact Information for Business Card

Marta Lindqvist
pediatric sleep consultant
+34 612 380 574

```html
<!DOCTYPE html>
<html lang="en">
<head>
<meta charset="utf-8">
<title>The Quiet Meadow Studio – Sleep Consultancy Flyer</title>
<link href="https://fonts.googleapis.com/css2?family=Raleway:wght@300;400;500&display=swap" rel="stylesheet">
<style>
:root{
  --rose:#e5897b;
  --rose-soft:#eea597;
  --text-grey:#8c9893;
  --heading-grey:#76857f;
  --panel:rgba(170,182,177,0.72);
  --panel-head:rgba(140,156,149,0.92);
  --white:#ffffff;
}
*{margin:0;padding:0;box-sizing:border-box}
html,body{width:849px;height:1200px;overflow:hidden;background:var(--white)}
body{font-family:'Raleway',sans-serif;font-weight:300;color:var(--text-grey)}
.flyer{position:relative;width:849px;height:1200px;overflow:hidden;background:var(--white)}

.hero-photo{position:absolute;left:0;top:0;width:420px;height:1071px;
  background:
    radial-gradient(ellipse 160px 420px at 90px 260px,#f2c9b8 0%,rgba(242,201,184,0) 100%),
    radial-gradient(ellipse 170px 260px at 150px 700px,#f6d6c8 0%,rgba(246,214,200,0) 100%),
    radial-gradient(ellipse 260px 200px at 120px 980px,#f3d2c4 0%,rgba(243,210,196,0) 100%),
    linear-gradient(90deg,#f4d8cc 0%,#fbece6 45%,rgba(255,255,255,0) 100%);}

.content{position:absolute;left:287px;width:528px}
.section-title{font-weight:400;color:var(--rose);font-size:24px;line-height:1.2}
.lead{font-weight:400;color:var(--heading-grey);font-size:19px;margin-top:10px;margin-bottom:4px}
.points{list-style:none}
.points li{position:relative;padding-left:19px;font-size:19.5px;line-height:24.3px;margin-bottom:6px;text-align:justify}
.points li::before{content:"";position:absolute;left:2px;top:9px;width:8px;height:8px;border-radius:50%;background:var(--text-grey)}
.need{top:56px}
.offer{top:449px}

.consult-panel{position:absolute;left:256px;top:767px;width:593px;height:304px;background:var(--panel)}
.consult-head{height:57px;background:var(--panel-head);color:var(--white);font-weight:400;font-size:24px;padding:14px 0 0 31px}
.consult-body{padding:16px 30px 0 31px;color:var(--white);font-size:19.5px;line-height:24.3px}
.consult-body p{margin-bottom:10px}

.footer-band{position:absolute;left:0;top:1071px;width:849px;height:129px;background:var(--rose);color:var(--white)}
.portrait{position:absolute;left:31px;top:938px;width:188px;height:188px;border-radius:50%;background:var(--rose-soft);padding:8px}
.portrait span{display:block;width:100%;height:100%;border-radius:50%;background:linear-gradient(160deg,#d9c3a5 0%,#ead9cc 55%,#3a3436 100%)}
.consultant{position:absolute;left:0;top:58px;width:244px;text-align:center}
.consultant-name{font-weight:400;font-size:21px}
.consultant-role{font-weight:400;font-size:15px;margin-top:6px}
.divider{position:absolute;top:25px;width:1px;height:92px;background:var(--white)}
.contact{position:absolute;left:254px;top:36px;font-size:14.5px;line-height:25px;font-weight:400}
.brand{position:absolute;left:550px;top:30px;width:299px;text-align:center}
.brand-mark{width:46px;height:46px;border:1.5px solid var(--white);border-radius:50%;margin:0 auto 10px}
.brand-name{font-weight:300;font-size:22px}
</style>
</head>
<body>
<div class="flyer">
  <div class="hero-photo" role="img" aria-label="Soft close-up photograph of a parent's hand holding a baby's tiny hand"></div>

  <section class="content need">
    <h2 class="section-title">Do I need a sleep consultant for my child?</h2>
    <p class="lead">The answer is yes if:</p>
    <ul class="points">
      <li>If your child will only fall asleep when nursing or bottle feeding</li>
      <li>If your child needs a dummy or other external aid, like being rocked, patted or taken for a care ride to fall asleep</li>
      <li>If your good night routine is a challenging and exhausting procedure instead of a relaxed and enjoyable moment for the whole family</li>
      <li>If sleep is a constant battle in your home which leaves you feeling frustrated and exhausted</li>
      <li>If your own lack of sleep is taking a toll on you and the whole family</li>
    </ul>
  </section>

  <section class="content offer">
    <h2 class="section-title">What can I do for you?</h2>
    <p class="lead">I will :</p>
    <ul class="points">
      <li>Guide you to set an age appropriate foundation for good sleep</li>
      <li>Create an individual sleep plan tailored especially to your child’s sleep needs and circumstances</li>
      <li>Help you to teach your childto go to sleep and get back to sleep independently during the night</li>
      <li>show you how to teach your child to take healthful, restorative naps</li>
    </ul>
  </section>

  <section class="consult-panel">
    <h2 class="consult-head">FREE 15 minute consultation</h2>
    <div class="consult-body">
      <p>This 15 minute “mini” consultation is a chance to discuss your unique sleep challenges and sleep goals with me. I will provide you with an overview of how I will work with your family to achieve your wildest sleep dreams (goals).</p>
      <p>Furthermore do I understand and believe that every child and their family is unique and there is no one size fits all!</p>
      <p>I would love to have a chat with you and talk about how I can help make things easier for you and your family!</p>
    </div>
  </section>

  <footer class="footer-band">
    <div class="consultant">
      <div class="consultant-name">Marta Lindqvist</div>
      <div class="consultant-role">Certified Sleep Consultant</div>
    </div>
    <span class="divider" style="left:244px"></span>
    <div class="contact">
      info@quietmeadowstudio-example.com<br>
      www.quietmeadowstudio-example.com<br>
      +34 612 380 574
    </div>
    <span class="divider" style="left:534px"></span>
    <div class="brand">
      <div class="brand-mark"></div>
      <div class="brand-name">The Quiet Meadow Studio</div>
    </div>
  </footer>

  <div class="portrait"><span role="img" aria-label="Portrait photo of the sleep consultant"></span></div>
</div>
</body>
</html>
```